Diagramm/Grafik zur Darstellung einer Formel
Zielgruppe
Das Unternehmen ist in der Unternehmensberatung tätig und beschäftigt sich mit der Analyse von IT-In- und Outsourcing.
Zielgruppe: Entscheider / Höheres Management / Round Table
Aufgabenstellung
Es wurde für die Bewertung des bestehenden Outsourcing eine Formel entwickelt, welche es ermöglicht einerseits die Stärken
und Schwächen und andererseits die Entwicklung und Vorteilhaftigkeit der Kosten für die nächsten Jahre zu prognostizieren.
Der Name der Formel ist "MIRAX-P Methode" (Strategie, Technologie, Organisation, Qualität und Kosten)
Die Formel ist aufgebaut aus 5 Sektoren, unter welchem jeweils 3-8 Faktoren untergeordnet sind. (siehe IMG_1159)
Die Zuordnung der Faktoren zu Sektoren (siehe SektorenFaktoren.pdf) ist variabel, aus welchem Grund unter jedem Sektor 3-8 Faktoren unterordnenbar sein sollten.
Grundsätzlich findet die Auswertung aus dem Vergleich von Kosten + Risiken - Chancen jeweils von Outsourcing und Insourcing statt. (siehe IMG_1190)
Ziel ist es, eine Darstellung der Sektoren und Faktoren sowie der Formel zu finden, welche:
a) die Abhängigkeit von den Faktoren zu den Sektoren darstellt
b) die Formel darstellt
c) sich als Ganzes oder in Teilen für diverse Unterlagen verwenden lässt (bspw. .pptx, .pdf, etc.)
--> es ist geplant diese Darstellung bspw. als Ganzes oder in Teilen in eine PowerPoint-Präsentation zu integrieren
Diese Aufgabenstellung ist ein erster Versuch mittels der Plattform pixelhafen.de Aufträge zu vergeben.
Bei Erfolg sind Anschlussaufträge geplant.
WICHTIG: Alle Anhänge diesen lediglich zur Darstellung der Zusammenhänge, sollen aber keinerlei design vorgeben!

```html
<!DOCTYPE html>
<html lang="de">
<head>
<meta charset="utf-8">
<title>MIRAX-P Methode</title>
<link href="https://fonts.googleapis.com/css2?family=Open+Sans:wght@400;600;700;800&display=swap" rel="stylesheet">
<style>
  :root {
    --brand-blue: #27a9e1;
    --ink: #1a1a1a;
    --rule: #8a8a8a;
    --paper: #ffffff;
  }
  * { margin: 0; padding: 0; box-sizing: border-box; }
  html, body { width: 848px; height: 1200px; overflow: hidden; background: var(--paper); }
  .sheet {
    position: relative;
    width: 848px;
    height: 1200px;
    font-family: "Open Sans", Arial, sans-serif;
    color: var(--ink);
  }
  .title {
    position: absolute;
    left: 18px;
    top: 4px;
    font-size: 74px;
    font-weight: 700;
    letter-spacing: -0.5px;
    line-height: 1.1;
  }
  .connectors { position: absolute; left: 0; top: 0; }
  .formula {
    position: absolute;
    top: 126px;
    font-size: 30px;
    font-weight: 700;
    line-height: 1;
    white-space: nowrap;
  }
  .formula--os { left: 28px; }
  .formula--is { left: 441px; }
  .comparator {
    position: absolute;
    left: 405px;
    top: 139px;
    font-size: 13px;
    font-weight: 600;
    transform: rotate(90deg);
    transform-origin: center;
  }
  .column {
    position: absolute;
    top: 214px;
    width: 380px;
    height: 923px;
  }
  .column--os { left: 28px; }
  .column--is { left: 437px; }
  .column__spine {
    position: absolute;
    left: 0; top: 0;
    width: 31px; height: 100%;
    background: var(--brand-blue);
  }
  .sector {
    position: absolute;
    left: 0;
    width: 100%;
    height: 189px;
  }
  .sector:nth-of-type(1) { top: 0; }
  .sector:nth-of-type(2) { top: 189px; }
  .sector:nth-of-type(3) { top: 380px; }
  .sector:nth-of-type(4) { top: 567px; }
  .sector:nth-of-type(5) { top: 755px; }
  .sector__title {
    width: 316px;
    height: 41px;
    background: var(--brand-blue);
    color: var(--paper);
    font-size: 27px;
    font-weight: 700;
    line-height: 41px;
    padding-left: 4px;
    letter-spacing: -0.3px;
  }
  .factors {
    list-style: none;
    margin-left: 35px;
    width: 322px;
  }
  .factors li {
    height: 15px;
    border-bottom: 1px solid var(--rule);
    font-size: 14px;
    line-height: 14px;
    letter-spacing: -0.2px;
    white-space: nowrap;
  }
  .sector__sum {
    position: absolute;
    left: 255px;
    top: 161px;
    width: 100px;
    text-align: right;
    font-size: 14px;
    font-weight: 700;
  }
</style>
</head>
<body>
<main class="sheet">
  <h1 class="title">MIRAX-P Methode</h1>

  <svg class="connectors" width="848" height="1200" aria-hidden="true">
    <polyline points="30,214 100,164 332,164" fill="none" stroke="var(--brand-blue)" stroke-width="3"/>
    <polyline points="439,214 506,164 741,164" fill="none" stroke="var(--brand-blue)" stroke-width="3"/>
  </svg>

  <div class="formula formula--os">OS+(Chancen - Risiken)</div>
  <div class="comparator">&lt;=&gt;</div>
  <div class="formula formula--is">IS+(Chancen - Risiken)</div>

  <section class="column column--os">
    <div class="column__spine"></div>
    <div class="sector">
      <h2 class="sector__title">Strategie</h2>
      <ul class="factors">
        <li>komparativer Konkurrenzvorteil</li>
        <li>Kernkompetenz</li>
        <li>Wertschöpfungstiefe</li>
        <li>Marktbewegung</li>
        <li>Marktein- / -austrittsstrategie</li>
        <li>Sourcing- / Vendorstrategie</li>
        <li>Risikoabsicherung</li>
        <li>Ungewissheit</li>
      </ul>
      <div class="sector__sum">Summe</div>
    </div>
    <div class="sector">
      <h2 class="sector__title">Technologie</h2>
      <ul class="factors">
        <li>Innovationsrate</li>
        <li>Synergien</li>
        <li>Portfolio-Erweiterung</li>
        <li>Best-Practices</li>
        <li></li><li></li><li></li><li></li>
      </ul>
      <div class="sector__sum">Summe</div>
    </div>
    <div class="sector">
      <h2 class="sector__title">Organisation</h2>
      <ul class="factors">
        <li>Wissen</li>
        <li>Kommunikation</li>
        <li>Umsetzungsgeschwindigkeit</li>
        <li>Flexibilität</li>
        <li>Skalierbarkeit</li>
        <li>Time-to-Market</li>
        <li>Organisationstransformation</li>
        <li></li>
      </ul>
      <div class="sector__sum">Summe</div>
    </div>
    <div class="sector">
      <h2 class="sector__title">Qualität</h2>
      <ul class="factors">
        <li>Kontroll- und Prüfaufwände</li>
        <li>Compliance (legal)</li>
        <li>Sprach- /Kulturbarrieren</li>
        <li>Distanz / Nähe</li>
        <li></li><li></li><li></li><li></li>
      </ul>
      <div class="sector__sum">Summe</div>
    </div>
    <div class="sector">
      <h2 class="sector__title">Qualität</h2>
      <ul class="factors">
        <li>Management-Kosten</li>
        <li>Vertragsänderungs-/</li>
        <li>-verwaltungskosten</li>
        <li>Cash Flow</li>
        <li>Return-on-Invest</li>
        <li>fixe vs. Variable Kosten Kosten</li>
        <li>Tax</li>
        <li></li>
      </ul>
      <div class="sector__sum">Summe</div>
    </div>
  </section>

  <section class="column column--is">
    <div class="column__spine"></div>
    <div class="sector">
      <h2 class="sector__title">Strategie</h2>
      <ul class="factors">
        <li>komparativer Konkurrenzvorteil</li>
        <li>Kernkompetenz</li>
        <li>Wertschöpfungstiefe</li>
        <li>Marktbewegung</li>
        <li>Marktein- / -austrittsstrategie</li>
        <li>Sourcing- / Vendorstrategie</li>
        <li>Risikoabsicherung</li>
        <li>Ungewissheit</li>
      </ul>
      <div class="sector__sum">Summe</div>
    </div>
    <div class="sector">
      <h2 class="sector__title">Technologie</h2>
      <ul class="factors">
        <li>Innovationsrate</li>
        <li>Synergien</li>
        <li>Portfolio-Erweiterung</li>
        <li>Best-Practices</li>
        <li></li><li></li><li></li><li></li>
      </ul>
      <div class="sector__sum">Summe</div>
    </div>
    <div class="sector">
      <h2 class="sector__title">Organisation</h2>
      <ul class="factors">
        <li>Wissen</li>
        <li>Kommunikation</li>
        <li>Umsetzungsgeschwindigkeit</li>
        <li>Flexibilität</li>
        <li>Skalierbarkeit</li>
        <li>Time-to-Market</li>
        <li>Organisationstransformation</li>
        <li></li>
      </ul>
      <div class="sector__sum">Summe</div>
    </div>
    <div class="sector">
      <h2 class="sector__title">Qualität</h2>
      <ul class="factors">
        <li>Kontroll- und Prüfaufwände</li>
        <li>Compliance (legal)</li>
        <li>Sprach- /Kulturbarrieren</li>
        <li>Distanz / Nähe</li>
        <li></li><li></li><li></li><li></li>
      </ul>
      <div class="sector__sum">Summe</div>
    </div>
    <div class="sector">
      <h2 class="sector__title">Qualität</h2>
      <ul class="factors">
        <li>Management-Kosten</li>
        <li>Vertragsänderungs-/</li>
        <li>-verwaltungskosten</li>
        <li>Cash Flow</li>
        <li>Return-on-Invest</li>
        <li>fixe vs. Variable Kosten Kosten</li>
        <li>Tax</li>
        <li></li>
      </ul>
      <div class="sector__sum">Summe</div>
    </div>
  </section>
</main>
</body>
</html>
```